Full Page Appliance Ad

Create a full page ad (7.5" W x 10" H) representing that we are a full service appliance company, where we have a showroom located at 14 N. Birch Lane Souderton, PA 18970. Our website is www.qrtolvek.com , and our phone number is 215-555-0148. We don't only sell appliances, we deliver, install, and service. We also offer an additional year warranty* (see store for details). In addition to appliances, we also have an Electrical Department that specializes in residential applications.
May be best if split the full page ad into two spots. One spot to reference appliances, and the other to represent electrical.
I want it to look clean, and not too busy
Target Market(s)
30-70 years old
Look and feel

```html
<!DOCTYPE html>
<html lang="en">
<head>
<meta charset="utf-8">
<title>Qrtolvek and Son Inc — Appliances &amp; Electrical</title>
<link href="https://fonts.googleapis.com/css2?family=Alice&family=Barlow:wght@400;500&family=Dancing+Script:wght@600&family=Lora&display=swap" rel="stylesheet">
<style>
  :root {
    --stage: #d9d9dc;
    --paper: #efe7d6;
    --band: #d8dee1;
    --ink: #1b1b1b;
    --brand: #1f2a4a;
    --frame: #7b6a5b;
    --photo-light: #e9e6e0;
    --photo-mid: #c9c3ba;
    --photo-dark: #8e8378;
  }
  * { margin: 0; padding: 0; box-sizing: border-box; }
  html, body { width: 1200px; height: 540px; overflow: hidden; background: var(--stage); }
  .canvas { position: relative; width: 1200px; height: 540px; }

  .flyer {
    position: absolute; left: 409px; top: 0;
    width: 382px; height: 540px;
    background: var(--paper);
    color: var(--ink);
    overflow: hidden;
  }
  .band { position: absolute; left: 19.5px; width: 342px; background: var(--band); }
  .band--top { top: 0; height: 31.5px; border-bottom: 1px solid var(--ink); }
  .band--bottom { top: 507px; height: 33px; border-top: 1px solid var(--ink); }
  .rule { position: absolute; left: 19.5px; width: 342px; height: 1px; background: var(--ink); }

  .tagline {
    position: absolute; left: 0; width: 100%; top: 33px;
    text-align: center;
    font-family: "Dancing Script", cursive; font-weight: 600; font-size: 15px;
  }
  .warranty-badge {
    position: absolute; left: 165.5px; top: 73.5px;
    width: 57px; height: 57px; border: 1.5px solid var(--ink); border-radius: 50%;
    display: flex; align-items: center; justify-content: center;
    font-family: "Barlow", sans-serif; font-size: 17px; letter-spacing: 0.5px;
  }
  .headline {
    position: absolute; left: 0; width: 100%; top: 143px;
    text-align: center;
    font-family: "Alice", serif; font-size: 26.5px; font-weight: 400;
  }
  .intro {
    position: absolute; top: 190px; width: 135px;
    font-family: "Barlow", sans-serif; font-size: 6.9px; line-height: 8.9px;
  }
  .intro--appliances { left: 41.5px; }
  .intro--electrical { left: 206.5px; }
  .intro-divider { position: absolute; left: 189px; top: 193px; width: 1px; height: 32px; background: var(--ink); }

  .photo {
    position: absolute; left: 53.5px; top: 237.5px; width: 271px; height: 181.5px;
    border: 3.5px solid var(--frame);
    background: linear-gradient(100deg, var(--photo-light) 0%, #ddd8d0 40%, var(--photo-mid) 65%, var(--photo-dark) 100%);
  }

  .brand {
    position: absolute; left: 0; width: 100%; top: 424px;
    display: flex; align-items: center; justify-content: center; gap: 6px;
    color: var(--brand);
  }
  .brand-mark { width: 30px; height: 30px; border: 1.5px solid var(--brand); border-radius: 50%; }
  .brand-name { font-family: "Barlow", sans-serif; font-weight: 500; font-size: 11px; line-height: 12px; letter-spacing: 0.5px; text-transform: uppercase; }

  .contact {
    position: absolute; top: 467px; height: 19px;
    display: flex; align-items: center;
    font-family: "Barlow", sans-serif; font-size: 7.4px;
  }
  .contact--address { left: 27.5px; }
  .contact--phone { left: 217px; }
  .contact-divider { position: absolute; left: 191px; top: 463px; width: 1px; height: 23.5px; background: var(--ink); }

  .web {
    position: absolute; left: 0; width: 100%; top: 516px;
    text-align: center;
    font-family: "Lora", serif; font-size: 7.5px;
  }
</style>
</head>
<body>
<main class="canvas">
  <article class="flyer">
    <div class="band band--top"></div>
    <p class="tagline">your full service appliance company</p>
    <div class="rule" style="top:53.5px"></div>

    <div class="warranty-badge">+1 YR</div>
    <h1 class="headline">Appliances &amp; Electrical</h1>

    <p class="intro intro--appliances">Appliances: visit our showroom for the brands you trust. We sell, deliver, install and service every one, plus an additional year warranty* (*see store for details).</p>
    <div class="intro-divider"></div>
    <p class="intro intro--electrical">Electrical: our Electrical Department specializes in residential applications, from new wiring and panels to lighting, outlets and repairs.</p>

    <div class="photo" role="img" aria-label="Photo of a bright kitchen with modern appliances"></div>

    <div class="brand">
      <span class="brand-mark"></span>
      <span class="brand-name">Qrtolvek<br>and Son Inc</span>
    </div>

    <div class="rule" style="top:463px"></div>
    <p class="contact contact--address">14 N. Birch Lane Souderton, PA 18970</p>
    <div class="contact-divider"></div>
    <p class="contact contact--phone">Call us at 215-555-0148</p>
    <div class="rule" style="top:486.5px"></div>

    <div class="band band--bottom"></div>
    <p class="web">www.qrtolvek.com</p>
  </article>
</main>
</body>
</html>
```